Brightfern Studios Company Wordpress Site

We need a new company site for an established game development studio in Dallas, Texas. It should be a much more professional look than we have now, but we still want it to be a bit fun. It needs to be built so we can add more content later (as we publish new games, gain new clients, etc).
This could be built as a single page, multi-page, or a hybrid design. The design must scale to fit desktop and mobile browsers. This job will require that the website be both designed, and coded in Wordpress.
Your design should include at least the following areas:
MAIN LANDING AREA
- The company logo.
- Basic company info with a call to action.
- Chirpline feed integration for news.
- Social media links.
GAMES AREA
- Section for games we have developed (logos and links).
- Second section for games we have ported (logos and links).
- This area should be designed to expand to many games.
SERVICES AREA
- Two or three paragraphs of text.
- A few images related to our services.
- FAQ about our services.
CONTACT AREA
- One or two paragraphs of text.
- Contact form.
ABOUT AREA
- Two or three paragraphs about the company.
- A few images about the company.
We will provide the final text and images to use on the site once a winning design is selected.
Again we need a more professional, modern, and more minimalist look than our current site (www.brightfernstudios-example.com), but are not opposed to something fun. We want to retain our current logo (included in the download). We know the name of the company is offbeat, but please avoid anything gross, dark, or violent, as professionalism is key. Leaning on our past projects is a good idea because we’ve worked with some very reputable game developers.
Need extra days to review
Hey everyone. We've received some fantastic submissions and want to continue working with a few of them for a little more time before making our decision. So we have extended the deadline and have also added 2nd and 3rd place rewards. Thanks to everybody who submitted!
Target Market(s)
Gamers, game professionals, developers, technology leaders, etc.
Industry/Entity Type
Games
Coding
Coded - Design and coding required
Look and feel
Each slider illustrates characteristics of the customer's brand and the style your logo design should communicate.

```html
<!DOCTYPE html>
<html lang="en">
<head>
<meta charset="utf-8">
<title>Brightfern Studios</title>
<link rel="stylesheet" href="https://fonts.googleapis.com/css2?family=Titillium+Web:wght@400;600;700&family=Open+Sans:wght@400&display=swap">
<style>
:root{
  --white:#ffffff;
  --ink:#111111;
  --muted:#333333;
  --rule:#d6d6d6;
  --accent:#1da1f2;
  --footer:#6b6b6b;
  --social-a:#3b5998;
  --social-b:#1da1f2;
  --social-c:#1a2f6b;
}
*{margin:0;padding:0;box-sizing:border-box}
html,body{width:1200px;height:1197px;overflow:hidden;background:var(--white)}
body{position:relative;font-family:"Titillium Web",sans-serif;color:var(--ink)}
.hero{position:absolute;left:0;top:0;width:1200px;height:736px;overflow:hidden}
.hero-photo{position:absolute;inset:0;
  background:
   radial-gradient(ellipse 360px 260px at 930px 330px, rgba(70,150,215,.85), rgba(30,70,110,0) 70%),
   radial-gradient(ellipse 300px 420px at 230px 300px, rgba(110,70,45,.7), rgba(40,30,25,0) 75%),
   linear-gradient(110deg,#1c1a1a 0%,#2a2622 35%,#1d2a38 60%,#16324c 80%,#0f1c2a 100%)}
.hero-shade{position:absolute;inset:0;background:linear-gradient(90deg,rgba(0,0,0,.35),rgba(0,0,0,0) 60%)}
.brand{position:absolute;left:40px;top:44px;color:var(--white);font-weight:700;font-size:34px;line-height:1;letter-spacing:.5px}
.brand small{display:block;font-size:34px}
.nav{position:absolute;top:18px;left:614px;display:flex;list-style:none}
.nav li{font-size:16px;font-weight:700;color:var(--white);height:26px;line-height:26px;padding:0 13px;margin-right:16px;letter-spacing:.3px}
.nav li.active{background:var(--white);color:var(--ink)}
.welcome{position:absolute;left:174px;top:384px;color:var(--white)}
.welcome h2{font-size:28px;font-weight:700;line-height:1}
.welcome h1{font-size:50px;font-weight:700;line-height:1;margin-top:16px;letter-spacing:.5px}
.welcome p{font-size:17.6px;line-height:21px;width:420px;margin-top:30px}
.btn{position:absolute;left:174px;top:603px;width:127px;height:40px;border:2px solid var(--white);border-radius:3px;color:var(--white);font-weight:700;font-size:17px;display:flex;align-items:center;justify-content:center}
.dots{position:absolute;left:0;top:0}
.feed-head{position:absolute;left:130px;top:796px;font-size:29px;font-weight:700;line-height:1}
.follow{position:absolute;left:270px;top:800px;width:80px;height:26px;background:var(--accent);border-radius:2px;color:var(--white);font-size:11.5px;font-weight:600;display:flex;align-items:center;justify-content:center;gap:5px}
.follow i{width:8px;height:8px;border-radius:50%;background:var(--white);display:block}
.arrows{position:absolute;left:1020px;top:802px}
.feed-rule{position:absolute;left:133px;top:843px;width:931px;height:2px;background:var(--rule)}
.post{position:absolute;top:911px;width:270px}
.post .avatar{position:absolute;left:0;top:0;width:52px;height:52px;border-radius:50%;background:radial-gradient(circle at 50% 40%,#9a7b66,#3b3d45)}
.post .who{position:absolute;left:75px;top:7px;font-size:14.4px;line-height:19px}
.post .who b{font-weight:600}
.post .time{position:absolute;left:199px;top:16px;font-family:"Open Sans",sans-serif;font-size:11px;color:var(--muted)}
.post p{position:absolute;left:1px;top:77px;width:250px;font-family:"Open Sans",sans-serif;font-size:13px;line-height:16px;color:var(--muted)}
.divider{position:absolute;top:900px;width:2px;height:148px;background:#e4e4e4}
.footer{position:absolute;left:0;top:1113px;width:1200px;height:84px;background:var(--footer);color:var(--white)}
.footer .mark{position:absolute;left:132px;top:24px;font-weight:700;font-size:18px;line-height:18px}
.footer .links{position:absolute;left:296px;top:33px;font-size:13.6px}
.footer .links span{margin:0 6px}
.footer .social{position:absolute;left:641px;top:30px;font-size:16px;display:flex;align-items:center}
.footer .social i{display:block;width:27px;height:27px;border-radius:50%;margin-left:7px}
.footer .social i:first-of-type{margin-left:16px}
.footer .copy{position:absolute;left:874px;top:35px;font-family:"Open Sans",sans-serif;font-size:11px}
</style>
</head>
<body>
<header class="hero">
  <div class="hero-photo" role="img" aria-label="Photo of a game developer working at a monitor showing a 3D level editor"></div>
  <div class="hero-shade"></div>
  <div class="brand">BRIGHTFERN<small>STUDIOS</small></div>
  <ul class="nav">
    <li class="active">HOME</li><li>GAMES</li><li>SERVICES</li><li>CONTACT</li><li>ABOUT</li>
  </ul>
  <div class="welcome">
    <h2>Welcome to</h2>
    <h1>BRIGHTFERN STUDIOS</h1>
    <p>Lorem Ipsum is simply dummy text of the printing and typesetting industry. Lorem Ipsum has been the industry's standard dummy text ever since</p>
  </div>
  <div class="btn">READ MORE</div>
  <svg class="dots" width="1200" height="736" aria-hidden="true">
    <g fill="#fff"><circle cx="548" cy="664" r="5"/><circle cx="571" cy="664" r="5"/><circle cx="620" cy="664" r="5"/><circle cx="651" cy="664" r="5"/></g>
    <circle cx="597" cy="665" r="6" fill="none" stroke="#fff" stroke-width="2"/>
  </svg>
</header>

<section class="feed">
  <h2 class="feed-head">CHIRPLINE</h2>
  <div class="follow"><i></i>FOLLOW</div>
  <svg class="arrows" width="50" height="20" aria-hidden="true" fill="none" stroke="#555" stroke-width="2">
    <polyline points="13,2 6,10 13,18"/><polyline points="37,2 44,10 37,18"/>
  </svg>
  <div class="feed-rule"></div>

  <article class="post" style="left:130px">
    <div class="avatar" role="img" aria-label="Profile photo"></div>
    <div class="who"><b>Corvin Hale</b><br>@corvinhale</div>
    <div class="time">11 mins</div>
    <p>There are many variations of passages of Lorem Ipsum available, but the majority have suffered.</p>
  </article>
  <div class="divider" style="left:427px"></div>
  <article class="post" style="left:478px">
    <div class="avatar" role="img" aria-label="Profile photo"></div>
    <div class="who"><b>Corvin Hale</b><br>@corvinhale</div>
    <div class="time">11 mins</div>
    <p>There are many variations of passages of Lorem Ipsum available, but the majority have suffered.</p>
  </article>
  <div class="divider" style="left:771px"></div>
  <article class="post" style="left:826px">
    <div class="avatar" role="img" aria-label="Profile photo"></div>
    <div class="who"><b>Corvin Hale</b><br>@corvinhale</div>
    <div class="time">11 mins</div>
    <p>There are many variations of passages of Lorem Ipsum available, but the majority have suffered.</p>
  </article>
</section>

<footer class="footer">
  <div class="mark">BRIGHTFERN<br>STUDIOS</div>
  <div class="links">Home<span>|</span>Games<span>|</span>Services<span>|</span>Content<span>|</span>About</div>
  <div class="social">FOLLOW US<i style="background:var(--social-a)"></i><i style="background:var(--social-b)"></i><i style="background:var(--social-c)"></i></div>
  <div class="copy">Copyrights @ 2018 All Rights Reserved</div>
</footer>
</body>
</html>
```